Letterhead and compliment slip

We are a UK-based market research agency. We are looking for a new letterhead design to incorporate our logo, address details and company information. We are looking for a simple design. It should be modern. It needs to have a qualify feel. As we are UK based it needs to be designed for A4 paper size (letterhead).
I'm really looking for something simple in design terms!
Both letterhead and compliment slip need to include:
Our logo
Company address
Telephone number
Email address
Website address
Company registration number
VAT registration number
Grey and green would be a good colour scheme to fit with our logo

```html
<!DOCTYPE html>
<html lang="en">
<head>
<meta charset="utf-8">
<title>Clearview – Letterhead and Compliment Slip</title>
<link href="https://fonts.googleapis.com/css2?family=Open+Sans:wght@400;600;700&display=swap" rel="stylesheet">
<style>
  :root{
    --green:#9cc634;
    --grey-bar:#b3b3b5;
    --ink:#3a3a3a;
    --muted:#8a8a8a;
    --paper:#ffffff;
    --backdrop:#e6e6e6;
  }
  *{box-sizing:border-box;margin:0;padding:0}
  html,body{width:1200px;height:880px;overflow:hidden}
  body{background:var(--backdrop);font-family:"Open Sans",Arial,sans-serif;color:var(--ink);position:relative}
  .sheet{position:absolute;background:var(--paper);box-shadow:0 2px 6px rgba(0,0,0,.18)}
  .letterhead{left:80px;top:86px;width:499px;height:707px}
  .slip{left:621px;top:558px;width:499px;height:236px}
  .edge{position:absolute;left:0;top:0;bottom:0;width:8px;display:flex;flex-direction:column}
  .edge span{flex:1;background:var(--green)}
  .edge span:nth-child(2){background:var(--grey-bar)}
  .brand{position:absolute;display:flex;align-items:center;gap:6px}
  .brand-dot{width:16px;height:16px;border-radius:50%;background:var(--green)}
  .brand-name{font-weight:700;font-size:27px;color:var(--green);letter-spacing:-.3px;line-height:1}
  .contact{position:absolute;border-left:1px solid #bbb;padding-left:6px;font-size:7px;line-height:9px;color:var(--ink)}
  .contact li{list-style:none;display:flex;align-items:center;gap:4px}
  .contact svg{width:6px;height:6px;flex:none}
  .letterhead .brand{left:40px;top:34px}
  .letterhead .contact{left:350px;top:34px}
  .slip .brand{left:29px;top:20px}
  .slip .contact{left:358px;top:21px}
  .greeting{position:absolute;left:43px;top:164px;font-family:Arial,Helvetica,sans-serif;font-weight:700;font-size:12px;color:var(--green)}
  .body-copy{position:absolute;left:43px;top:196px;width:418px;font-size:10px;line-height:13.1px;text-align:justify;color:#444}
  .body-copy p{margin-bottom:13px}
  .signature{position:absolute;left:42px;top:500px;width:93px;height:46px;background:#ececec;border-radius:3px}
  .footer{position:absolute;left:41px;font-size:7px;line-height:12px}
  .letterhead .footer{top:676px}
  .slip .footer{left:29px;top:205px}
  .footer .address{color:var(--ink)}
  .footer .reg{color:var(--muted)}
</style>
</head>
<body>

<section class="sheet letterhead">
  <div class="edge"><span></span><span></span><span></span></div>
  <div class="brand"><div class="brand-dot"></div><div class="brand-name">Clearview</div></div>
  <ul class="contact">
    <li><svg viewBox="0 0 10 10"><path d="M2 1l2 2-1 1.5c.6 1.2 1.3 1.9 2.5 2.5L7 6l2 2-1.5 1.5C4 9 1 6 .5 2.5z" fill="#9cc634"/></svg>+44 (0)1632 960418</li>
    <li><svg viewBox="0 0 10 10"><rect x="0.5" y="2" width="9" height="6" fill="none" stroke="#9cc634" stroke-width="1.3"/><path d="M.5 2l4.5 3.5L9.5 2" fill="none" stroke="#9cc634" stroke-width="1.1"/></svg>hello@clearviewinsight.co.uk</li>
    <li><svg viewBox="0 0 10 10"><circle cx="5" cy="5" r="4.3" fill="none" stroke="#9cc634" stroke-width="1.2"/><path d="M.7 5h8.6M5 .7c-2.4 2.6-2.4 6 0 8.6M5 .7c2.4 2.6 2.4 6 0 8.6" fill="none" stroke="#9cc634" stroke-width=".8"/></svg>www.clearviewinsight.co.uk</li>
  </ul>

  <h1 class="greeting">Dear Mr. Ellis,</h1>
  <div class="body-copy">
    <p>Lorem Ipsum is simply dummy text of the printing and typesetting industry. Lorem Ipsum has been the industry's standard dummy text ever since the 1500s, when an unknown printer took a galley of type and scrambled it to make a type specimen book. It has survived not only five centuries, but also the leap into electronic typesetting, remaining essentially unchanged.</p>
    <p>The standard chunk of Lorem Ipsum used since the 1500s is reproduced below for those interested. Sections 1.10.32 and 1.10.33 from "de Finibus Bonorum et Malorum" by Aulus Fenn are also reproduced in their exact original form, accompanied by English versions from the 1914 translation by T. Mercer</p>
    <p>Lorem Ipsum is simply dummy text of the printing and typesetting industry. Lorem Ipsum has been the industry's standard dummy text ever since the 1500s, when an unknown printer took a galley of type and scrambled it to make a type specimen book. It has survived not only five centuries, but also the leap into electronic typesetting, remaining essentially unchanged. It was popularised in the</p>
    <p>The standard chunk of Lorem Ipsum used since the 1500s is reproduced below for those interested. Sections 1.10.32 and 1.10.33 from "de Finibus Bonorum et Malorum" by Aulus Fenn are also reproduced in their exact original form, accompanied by English versions from the 1914 translation by T. Mercer</p>
  </div>
  <div class="signature" role="img" aria-label="Handwritten signature of the sender"></div>

  <footer class="footer">
    <div class="address">12 Orchard House, Mill Lane, Kingsmead, Harpenden, Hertfordshire, UK, AL5 2QT</div>
    <div class="reg">Company registration number: 6041287 &nbsp;|&nbsp; VAT registration number: 731204958</div>
  </footer>
</section>

<section class="sheet slip">
  <div class="edge"><span></span><span></span><span></span></div>
  <div class="brand"><div class="brand-dot"></div><div class="brand-name">Clearview</div></div>
  <ul class="contact">
    <li><svg viewBox="0 0 10 10"><path d="M2 1l2 2-1 1.5c.6 1.2 1.3 1.9 2.5 2.5L7 6l2 2-1.5 1.5C4 9 1 6 .5 2.5z" fill="#9cc634"/></svg>+44 (0)1632 960418</li>
    <li><svg viewBox="0 0 10 10"><rect x="0.5" y="2" width="9" height="6" fill="none" stroke="#9cc634" stroke-width="1.3"/><path d="M.5 2l4.5 3.5L9.5 2" fill="none" stroke="#9cc634" stroke-width="1.1"/></svg>hello@clearviewinsight.co.uk</li>
    <li><svg viewBox="0 0 10 10"><circle cx="5" cy="5" r="4.3" fill="none" stroke="#9cc634" stroke-width="1.2"/><path d="M.7 5h8.6M5 .7c-2.4 2.6-2.4 6 0 8.6M5 .7c2.4 2.6 2.4 6 0 8.6" fill="none" stroke="#9cc634" stroke-width=".8"/></svg>www.clearviewinsight.co.uk</li>
  </ul>
  <footer class="footer">
    <div class="address">12 Orchard House, Mill Lane, Kingsmead, Harpenden, Hertfordshire, UK, AL5 2QT</div>
    <div class="reg">Company registration number: 6041287 &nbsp;|&nbsp; VAT registration number: 731204958</div>
  </footer>
</section>

</body>
</html>
```